Business card for massage therapy company called Brook Fern Wellness

Need business card for massage therapy company called Brook Fern Wellness. Would like my logo on the front and the back of the card I have 3 options of logos and you can play with what looks better.

Would like this information displayed on the back of the card:

Marcus Ellery
Licensed Massage Therapist
321-555-0147
brookfern-example.com
brookfern_rest_

```html
<!DOCTYPE html>
<html lang="en">
<head>
<meta charset="utf-8">
<title>Brook Fern Wellness — Business Card</title>
<link href="https://fonts.googleapis.com/css2?family=Marcellus&family=Montserrat:wght@400;500&display=swap" rel="stylesheet">
<style>
  :root {
    --stage: #2b2b2b;
    --card-front: #fbfaf8;
    --sage: #737a60;
    --sage-dark: #5f6650;
    --sage-faint: rgba(255, 255, 255, 0.12);
    --ink-light: #ffffff;
  }
  * { margin: 0; padding: 0; box-sizing: border-box; }
  html, body {
    width: 1200px; height: 689px; overflow: hidden;
    background: var(--stage);
  }
  .stage {
    width: 1200px; height: 689px;
    display: flex; align-items: center; justify-content: center; gap: 40px;
  }
  .card {
    width: 540px; height: 310px;
    border-radius: 18px;
    position: relative; overflow: hidden;
  }
  .card-front {
    background: var(--card-front);
    display: flex; align-items: center; justify-content: center;
  }
  .brand { display: flex; align-items: center; gap: 16px; }
  .brand-mark {
    width: 64px; height: 64px; border-radius: 50%;
    border: 1.5px solid var(--sage-dark);
  }
  .brand-name {
    font-family: "Marcellus", serif;
    color: var(--sage-dark);
    font-size: 30px; line-height: 1.15; letter-spacing: 3px;
    text-transform: uppercase;
  }
  .card-back {
    background: var(--sage);
    color: var(--ink-light);
  }
  .back-decoration {
    position: absolute; left: 70px; top: 40px;
    width: 250px; height: 250px; border-radius: 50%;
    border: 3px solid var(--sage-faint);
  }
  .identity {
    position: absolute; left: 48px; top: 122px;
    text-align: left;
  }
  .person-name {
    font-family: "Marcellus", serif;
    font-size: 30px; letter-spacing: 1px; text-transform: uppercase;
  }
  .person-role {
    font-family: "Montserrat", sans-serif;
    font-size: 14px; margin-top: 4px;
  }
  .divider {
    position: absolute; left: 330px; top: 100px;
    width: 1.5px; height: 110px; background: var(--ink-light);
  }
  .contact-list {
    position: absolute; left: 350px; top: 112px;
    list-style: none;
    font-family: "Montserrat", sans-serif; font-size: 12.5px;
  }
  .contact-item { display: flex; align-items: center; gap: 9px; height: 29px; }
  .contact-icon { width: 13px; height: 13px; flex: none; }
  .social-square {
    width: 11px; height: 11px; border: 1.5px solid var(--ink-light); border-radius: 2px; flex: none;
  }
</style>
</head>
<body>
<main class="stage">
  <section class="card card-front">
    <div class="brand">
      <span class="brand-mark"></span>
      <div class="brand-name">Brook Fern<br>Wellness</div>
    </div>
  </section>

  <section class="card card-back">
    <span class="back-decoration"></span>
    <div class="identity">
      <div class="person-name">Marcus Ellery</div>
      <div class="person-role">Licensed Massage Therapist</div>
    </div>
    <span class="divider"></span>
    <ul class="contact-list">
      <li class="contact-item">
        <svg class="contact-icon" viewBox="0 0 24 24" fill="#fff" aria-hidden="true">
          <path d="M6.6 10.8a15.2 15.2 0 0 0 6.6 6.6l2.2-2.2a1 1 0 0 1 1-.25 11.4 11.4 0 0 0 3.6.57 1 1 0 0 1 1 1V20a1 1 0 0 1-1 1A17 17 0 0 1 3 4a1 1 0 0 1 1-1h3.5a1 1 0 0 1 1 1c0 1.25.2 2.45.57 3.57a1 1 0 0 1-.25 1z"/>
        </svg>
        321-555-0147
      </li>
      <li class="contact-item">
        <svg class="contact-icon" viewBox="0 0 24 24" fill="none" stroke="#fff" stroke-width="2" aria-hidden="true">
          <circle cx="12" cy="12" r="10"/><path d="M2 12h20M12 2c3 3 3 17 0 20M12 2c-3 3-3 17 0 20"/>
        </svg>
        brookfern-example.com
      </li>
      <li class="contact-item">
        <span class="social-square"></span>
        brookfern_rest_
      </li>
    </ul>
  </section>
</main>
</body>
</html>
```